web site update

I want to get a better website for a small high end remodeling and construction company
I currently have a web site but you will find that it is not good.
www.pelbrookhaven.com
We are a high end construction / remodeling company that has been in business since 2003. We primarily work in the mid peninsula of the bay area. Most of our clientele are very educated captains of industry. This group is still the target client.
I had my logo designed by Vellum Forge a few years ago and I do like it, I like the orange and black or orange a blue. I don’t have a lot of content on hand as far as professional photographs.
Number of pages not sure and are open to: design pages vs full function website
I think what I am after is a web presence that will seal the deal as we are getting high referrals from past clients.
Construction
1 page

```html
<!DOCTYPE html>
<html lang="en">
<head>
<meta charset="utf-8">
<title>Pelbrook Haven Remodeling</title>
<link href="https://fonts.googleapis.com/css2?family=Lato:wght@300;400;700&family=Open+Sans:wght@400;600;700&display=swap" rel="stylesheet">
<style>
:root{
  --orange:#ff6a00;
  --orange-dark:#e85d00;
  --black:#000;
  --ink:#1b1b1b;
  --text:#333;
  --muted:#777;
  --grey-band:#ebebeb;
  --white:#fff;
  --field:#1e1e1e;
}
*{box-sizing:border-box;margin:0;padding:0}
html,body{width:1200px;height:2970px;overflow:hidden}
body{position:relative;background:var(--white);font-family:"Open Sans",sans-serif;color:var(--text)}
.abs{position:absolute}

/* header */
.site-header{position:absolute;left:0;top:0;width:1200px;height:118px;background:var(--white)}
.brand{position:absolute;left:75px;top:30px;display:flex;align-items:center;gap:14px}
.brand-square{width:44px;height:44px;background:var(--orange)}
.brand-name{font-family:"Open Sans",sans-serif;font-weight:700;font-size:19px;line-height:21px;color:var(--ink);letter-spacing:.5px;text-transform:uppercase}
.contact-strip{position:absolute;right:0;top:0;height:32px;display:flex;align-items:center}
.contact-email{font-size:12px;color:var(--muted);margin-right:34px;display:flex;align-items:center;gap:8px}
.contact-phone{height:32px;background:var(--black);color:var(--white);font-size:15px;font-weight:600;padding:0 44px 0 34px;border-bottom-left-radius:28px;display:flex;align-items:center;gap:10px}
.main-nav{position:absolute;right:60px;top:60px;display:flex;gap:34px}
.main-nav a{font-size:13px;color:var(--ink);text-decoration:none;letter-spacing:.8px;padding:0 10px 10px;text-transform:uppercase}
.main-nav a.is-active{border-bottom:2px solid var(--orange)}

/* hero */
.hero{position:absolute;left:0;top:118px;width:1200px;height:604px;overflow:hidden}
.hero-media{position:absolute;inset:0;background:linear-gradient(100deg,#93a7bd 0%,#b9c2c8 35%,#8c8f8d 58%,#c9a23a 72%,#4f6b8f 100%)}
.hero-title{position:absolute;left:110px;top:186px;font-family:"Lato",sans-serif;font-weight:400;font-size:51px;line-height:66px;color:var(--white)}
.hero-btn{position:absolute;left:110px;top:478px;width:210px;height:52px;background:var(--orange);color:var(--white);font-family:"Lato",sans-serif;font-size:25px;display:flex;align-items:center;justify-content:center}
.hero-arrow{position:absolute;top:282px;width:48px;height:56px;background:rgba(0,0,0,.35);display:flex;align-items:center;justify-content:center}
.hero-edge{position:absolute;left:0;top:640px}

/* section headings */
.section-mark{position:absolute;width:18px;height:18px;background:var(--black)}
.section-title{position:absolute;font-family:"Lato",sans-serif;font-weight:400;font-size:33px;color:var(--ink);text-transform:uppercase;letter-spacing:.5px;white-space:nowrap}
.section-title em{font-style:normal;color:var(--orange)}

/* projects */
.project{position:absolute;width:238px;height:215px;border:2px solid #d6d6d6}
.project-media{position:absolute;left:0;top:0;right:0;bottom:22px}
.project-caption{position:absolute;left:0;right:0;bottom:0;height:22px;background:var(--black);color:var(--white);font-size:11px;line-height:22px;padding-left:0;text-align:center}
.btn{position:absolute;background:var(--orange);color:var(--white);font-family:"Open Sans",sans-serif;font-size:16px;display:flex;align-items:center;justify-content:center;text-transform:uppercase}

/* about band */
.about-band{position:absolute;left:0;top:1490px;width:1200px;height:500px}
.about-sub{position:absolute;left:75px;top:1686px;font-size:13px;font-weight:700;color:var(--ink)}
.about-copy{position:absolute;left:75px;width:570px;font-size:11.5px;line-height:22px;color:var(--text)}
.testimonial-avatar{position:absolute;left:703px;top:1688px;width:70px;height:70px;border-radius:50%;border:3px solid var(--orange);background:radial-gradient(circle at 50% 40%,#d7dde2,#7e94a8)}
.testimonial-box{position:absolute;left:703px;top:1782px;width:386px;height:125px;background:var(--white);border:1px solid #cfcfcf;padding:14px 16px;font-size:11px;font-style:italic;line-height:21px;color:var(--text)}
.dots{position:absolute;right:10px;bottom:8px;display:flex;gap:6px}
.dots i{width:7px;height:7px;border-radius:50%;background:var(--ink)}
.dots i.on{background:var(--orange)}

/* services */
.service{position:absolute;width:320px;text-align:center}
.service h3{font-family:"Open Sans",sans-serif;font-weight:400;font-size:17px;color:var(--ink);margin:14px 0 12px;text-transform:uppercase}
.service p{font-size:12px;line-height:21px;color:var(--text)}

/* footer */
.footer-edge{position:absolute;left:0;top:2490px}
.site-footer{position:absolute;left:0;top:2540px;width:1200px;height:390px;background:var(--black)}
.footer-brand{position:absolute;left:530px;top:2535px;display:flex;align-items:center;gap:10px}
.footer-brand .brand-square{width:34px;height:34px}
.footer-brand .brand-name{color:var(--white);font-size:15px;line-height:17px}
.footer-col{position:absolute;top:2618px}
.footer-col h4{font-size:11px;font-weight:600;color:var(--white);text-transform:uppercase;padding-bottom:6px;border-bottom:2px solid var(--orange);display:inline-block;margin-bottom:26px}
.quick-links li{list-style:none;font-size:11px;color:#bbb;line-height:22px;display:flex;align-items:center;gap:12px}
.quick-links li::before{content:"";width:5px;height:5px;border-top:2px solid var(--orange);border-right:2px solid var(--orange);transform:rotate(45deg)}
.field{width:182px;height:28px;background:var(--field);border:1px solid #333;color:#888;font-size:10px;padding:7px 10px;margin-bottom:8px}
.field.tall{height:70px}
.submit{width:96px;height:24px;background:var(--orange);color:var(--white);font-size:10px;display:flex;align-items:center;justify-content:center;margin-top:10px;text-transform:uppercase}
.contact-row{display:flex;gap:12px;font-size:11px;color:#aaa;line-height:16px;margin-bottom:14px}
.contact-row svg{flex:none}
.map{width:222px;height:147px;background:linear-gradient(135deg,#e7e3d8,#cfd8c4 60%,#dfe3ea)}
.copyright-bar{position:absolute;left:0;top:2930px;width:1200px;height:40px;background:var(--orange);display:flex;align-items:center;justify-content:space-between;padding:0 75px;font-size:11px;color:var(--ink)}
.social{display:flex;gap:10px}
.social i{width:24px;height:24px;border:2px solid var(--ink);border-radius:50%}
</style>
</head>
<body>

<header class="site-header">
  <div class="brand">
    <span class="brand-square"></span>
    <span class="brand-name">Pelbrook Haven<br>Remodeling</span>
  </div>
  <div class="contact-strip">
    <span class="contact-email">
      <svg width="16" height="12" viewBox="0 0 16 12"><rect width="16" height="12" fill="#ff6a00"/><path d="M0 0 L8 7 L16 0" stroke="#fff" stroke-width="1.5" fill="none"/></svg>
      info@pelbrookhaven.com
    </span>
    <span class="contact-phone">
      <svg width="14" height="14" viewBox="0 0 24 24"><path fill="#fff" d="M6.6 10.8a15 15 0 0 0 6.6 6.6l2.2-2.2c.3-.3.7-.4 1-.2 1.1.4 2.3.6 3.6.6.6 0 1 .4 1 1V20c0 .6-.4 1-1 1C10.6 21 3 13.4 3 4c0-.6.4-1 1-1h3.5c.6 0 1 .4 1 1 0 1.2.2 2.4.6 3.6.1.3 0 .7-.2 1z"/></svg>
      415.555.0148
    </span>
  </div>
  <nav class="main-nav">
    <a class="is-active">Home</a><a>About Us</a><a>Contact Us</a><a>Gallery</a><a>Testimonials</a>
  </nav>
</header>

<section class="hero">
  <div class="hero-media" role="img" aria-label="Builder holding a yellow hard hat and rolled plans in front of a blurred construction site"></div>
  <h1 class="hero-title">A quality line of<br>construction<br>products and<br>services</h1>
  <span class="hero-btn">Learn More</span>
  <span class="hero-arrow" style="left:0"><svg width="18" height="28" viewBox="0 0 18 28"><path d="M15 2 L3 14 L15 26" stroke="#fff" stroke-width="3" fill="none"/></svg></span>
  <span class="hero-arrow" style="right:0"><svg width="18" height="28" viewBox="0 0 18 28"><path d="M3 2 L15 14 L3 26" stroke="#fff" stroke-width="3" fill="none"/></svg></span>
</section>
<svg class="hero-edge" width="1200" height="90" viewBox="0 0 1200 90">
  <polygon points="0,20 600,74 1200,20 1200,90 0,90" fill="#fff"/>
  <polyline points="0,22 600,76 1200,22" fill="none" stroke="#ff6a00" stroke-width="8"/>
</svg>

<span class="section-mark" style="left:591px;top:784px"></span>
<h2 class="section-title" style="left:450px;top:808px">Current <em>Projects</em></h2>

<div class="project" style="left:75px;top:883px"><div class="project-media" role="img" aria-label="Bulldozer grading earth" style="background:linear-gradient(160deg,#8c8f94,#c9b58a)"></div><div class="project-caption">Modren House</div></div>
<div class="project" style="left:345px;top:883px"><div class="project-media" role="img" aria-label="Team in hard hats reviewing plans on a laptop" style="background:linear-gradient(160deg,#e7e7e7,#8a98a8)"></div><div class="project-caption">Cloud Project</div></div>
<div class="project" style="left:614px;top:883px"><div class="project-media" role="img" aria-label="Large yellow mining truck" style="background:linear-gradient(180deg,#9db9d9,#d7b73a 55%,#6f6a63)"></div><div class="project-caption">Beautiful penthouse</div></div>
<div class="project" style="left:883px;top:883px"><div class="project-media" role="img" aria-label="Glass tower under construction with crane" style="background:linear-gradient(180deg,#3f8fd6,#9fc3e8)"></div><div class="project-caption">Mountain View</div></div>
<div class="project" style="left:75px;top:1129px"><div class="project-media" role="img" aria-label="Hand holding an orange hard hat" style="background:linear-gradient(160deg,#dfe8ea,#e9a03a 60%,#c9d3d8)"></div><div class="project-caption">Gercyle Project</div></div>
<div class="project" style="left:345px;top:1129px"><div class="project-media" role="img" aria-label="Engineers inspecting rooftop equipment" style="background:linear-gradient(160deg,#c5ccd2,#5c6670)"></div><div class="project-caption">Vacation Rentals</div></div>
<div class="project" style="left:614px;top:1129px"><div class="project-media" role="img" aria-label="Curved glass walkway with city view" style="background:linear-gradient(160deg,#dbe6ee,#7d98ac)"></div><div class="project-caption">Corporate Apartments</div></div>
<div class="project" style="left:883px;top:1129px"><div class="project-media" role="img" aria-label="Carpenter fitting a wooden frame" style="background:linear-gradient(160deg,#eee6da,#b89a74)"></div><div class="project-caption">Unfurnished</div></div>

<span class="btn" style="left:505px;top:1402px;width:192px;height:51px">View All</span>

<svg class="about-band" width="1200" height="500" viewBox="0 0 1200 500">
  <polygon points="0,58 600,8 1200,58 1200,500 0,500" fill="#ebebeb"/>
  <polyline points="0,56 600,6 1200,56" fill="none" stroke="#ff6a00" stroke-width="7"/>
</svg>

<span class="section-mark" style="left:75px;top:1600px"></span>
<h2 class="section-title" style="left:75px;top:1626px">Welcome to <em>Pelbrook</em> Haven</h2>
<p class="about-sub">Why Choose Pelbrook Haven?</p>
<p class="about-copy" style="top:1712px">Lorem Ipsum is simply dummy text of the printing and typesetting industry. Lorem Ipsum has been the industry's standard dummy text ever since the 1500s, when an unknown printer took a galley of type and scrambled it to make a type specimen book. It has survived not only five centuries, but also the leap into electronic typesetting, remaining essentially unchanged.</p>
<p class="about-copy" style="top:1822px">It was popularised in the 1960s with the release of Letraset sheets containing Lorem Ipsum passages, and more recently with desktop publishing software like Aldus PageMaker including versions of Lorem Ipsum.</p>
<span class="btn" style="left:75px;top:1892px;width:208px;height:51px;text-transform:none">Read More</span>

<span class="section-mark" style="left:703px;top:1600px"></span>
<h2 class="section-title" style="left:703px;top:1626px">Client <em>Testimonials</em></h2>
<div class="testimonial-avatar" role="img" aria-label="Client portrait"></div>
<div class="testimonial-box">Lorem Ipsum is simply dummy text of the printing and typesetting industry. Lorem Ipsum has been the industry's standard dummy text ever since the 1500s, when an unknown printer took a galley of type and scrambled it to make a type specimen book.
  <span class="dots"><i></i><i class="on"></i><i></i><i></i></span>
</div>

<span class="section-mark" style="left:591px;top:2052px"></span>
<h2 class="section-title" style="left:491px;top:2078px">Our <em>Services</em></h2>

<div class="service" style="left:88px;top:2152px">
  <svg width="46" height="46" viewBox="0 0 46 46"><g fill="none" stroke="#ff6a00" stroke-width="2.5"><path d="M6 16 L10 5 H36 L40 16 Z"/><path d="M6 16 H40"/><path d="M9 18 V41 H37 V18"/><rect x="19" y="27" width="8" height="14"/></g></svg>
  <h3>Civil Engineering</h3>
  <p>Lorem Ipsum is simply dummy text of the printing and typesetting industry. Lorem Ipsum has been the industry's standard dummy text ever since the 1500s, when an unknown printer took</p>
</div>
<div class="service" style="left:440px;top:2152px">
  <svg width="46" height="46" viewBox="0 0 46 46"><g fill="none" stroke="#ff6a00" stroke-width="2.5"><circle cx="23" cy="23" r="7"/><path d="M20 4 h6 l1 5 4 2 4-3 4 4-3 4 2 4 5 1 v6 l-5 1-2 4 3 4-4 4-4-3-4 2-1 5 h-6 l-1-5-4-2-4 3-4-4 3-4-2-4-5-1 v-6 l5-1 2-4-3-4 4-4 4 3 4-2 Z"/></g></svg>
  <h3>Industrial Engeering</h3>
  <p>Lorem Ipsum is simply dummy text of the printing and typesetting industry. Lorem Ipsum has been the industry's standard dummy text ever since the 1500s, when an unknown printer took</p>
</div>
<div class="service" style="left:792px;top:2152px">
  <svg width="46" height="46" viewBox="0 0 46 46"><g fill="none" stroke="#ff6a00" stroke-width="2.5"><path d="M8 38 L11 27 L32 6 L40 14 L19 35 Z"/><path d="M28 10 L36 18"/><path d="M11 27 L19 35"/></g></svg>
  <h3>Architectural Services</h3>
  <p>Lorem Ipsum is simply dummy text of the printing and typesetting industry. Lorem Ipsum has been the industry's standard dummy text ever since the 1500s, when an unknown printer took</p>
</div>

<span class="btn" style="left:504px;top:2386px;width:192px;height:52px;text-transform:uppercase">Free Consultation</span>

<svg class="footer-edge" width="1200" height="60" viewBox="0 0 1200 60">
  <polygon points="0,52 600,8 1200,52 1200,60 0,60" fill="#000"/>
  <polyline points="0,50 600,6 1200,50" fill="none" stroke="#ff6a00" stroke-width="7"/>
</svg>
<footer class="site-footer"></footer>
<div class="footer-brand">
  <span class="brand-square"></span>
  <span class="brand-name">Pelbrook Haven<br>Remodeling</span>
</div>

<div class="footer-col" style="left:75px">
  <h4>Quick Links</h4>
  <ul class="quick-links">
    <li>Home</li><li>About</li><li>Services</li><li>Projects</li><li>Gallery</li><li>Join Us</li><li>Contact Us</li>
  </ul>
</div>
<div class="footer-col" style="left:337px">
  <h4>Quick Inquiry</h4>
  <div class="field">Name</div>
  <div class="field">Email</div>
  <div class="field tall">Message</div>
  <div class="submit">Submit</div>
</div>
<div class="footer-col" style="left:598px">
  <h4>Contact Details</h4>
  <div class="contact-row"><svg width="12" height="16" viewBox="0 0 12 16"><path fill="#ff6a00" d="M6 0a6 6 0 0 0-6 6c0 4.5 6 10 6 10s6-5.5 6-10a6 6 0 0 0-6-6zm0 8.5A2.5 2.5 0 1 1 6 3.5a2.5 2.5 0 0 1 0 5z"/></svg><span>Pelbrook Haven Remodeling<br><small>128 Oak Lane, Suite 4<br>Menlo Park, CA</small></span></div>
  <div class="contact-row"><svg width="14" height="14" viewBox="0 0 24 24"><path fill="#ff6a00" d="M6.6 10.8a15 15 0 0 0 6.6 6.6l2.2-2.2c.3-.3.7-.4 1-.2 1.1.4 2.3.6 3.6.6.6 0 1 .4 1 1V20c0 .6-.4 1-1 1C10.6 21 3 13.4 3 4c0-.6.4-1 1-1h3.5c.6 0 1 .4 1 1 0 1.2.2 2.4.6 3.6.1.3 0 .7-.2 1z"/></svg><span>+(415) 555 0190</span></div>
  <div class="contact-row"><svg width="14" height="14" viewBox="0 0 24 24"><path fill="#ff6a00" d="M6.6 10.8a15 15 0 0 0 6.6 6.6l2.2-2.2c.3-.3.7-.4 1-.2 1.1.4 2.3.6 3.6.6.6 0 1 .4 1 1V20c0 .6-.4 1-1 1C10.6 21 3 13.4 3 4c0-.6.4-1 1-1h3.5c.6 0 1 .4 1 1 0 1.2.2 2.4.6 3.6.1.3 0 .7-.2 1z"/></svg><span>+(415) 555 0190</span></div>
  <div class="contact-row"><svg width="14" height="11" viewBox="0 0 16 12"><rect width="16" height="12" fill="#ff6a00"/><path d="M0 0 L8 7 L16 0" stroke="#000" stroke-width="1.5" fill="none"/></svg><span>hello@pelbrookhaven.com</span></div>
</div>
<div class="footer-col" style="left:859px">
  <h4>Location Map</h4>
  <div class="map" role="img" aria-label="Street map showing the office location"></div>
</div>

<div class="copyright-bar">
  <span>Copyright © 2016 pelbrookhaven.com. All Right Reserved.</span>
  <span class="social"><i></i><i></i><i></i><i></i></span>
</div>

</body>
</html>
```